Car wrap design for Boxwillow

We need a car wrap design for our Van (Korvana Stelt Hi roof Black color). We are freight expert sending international parcels from China to New Zealand. Consonlidating parcels and save money for customers. We would like to see designs that use the color match our logo and final design should communicate our service and tell customer we are expert,Specializing in International Freight Forwarding within China's Trade Line.

Our website: www.boxwillow.co.nz Our phone: 09 4815396, We specialized: Sea Parcels, Air Parcels, Loose Cargo
in China Trade line

Target Market(s)

New Zealand small business

Industry/Entity Type

International Freight Fowarding

• Please refer to brand guideline

Requirements
Must have
• logo, website, phone, what we do (Sea Parcels, Air Parcels, Loose Cargo)
Nice to have
• Beautiful Lines or Graphics

```html
<!DOCTYPE html>
<html lang="en">
<head>
<meta charset="utf-8">
<title>Boxwillow – Van Wrap</title>
<link rel="stylesheet" href="https://fonts.googleapis.com/css2?family=Anton&family=Montserrat:wght@600;700;800&family=Barlow+Semi+Condensed:wght@700&display=swap">
<style>
  :root {
    --wrap-red: #d90b0b;
    --map-red: #c80a0a;
    --wrap-black: #0c0c0c;
    --glass: #1d2226;
    --trim: #2b2b2b;
    --white: #f6f6f6;
    --hub: #c9cdd1;
    --tyre: #151515;
    --backdrop: #eceef0;
  }
  html, body { margin: 0; padding: 0; overflow: hidden; background: var(--backdrop); }
  .canvas { width: 1200px; height: 688px; position: relative; overflow: hidden; background: var(--backdrop); }
  .van { display: block; width: 1200px; height: 688px; }
  .brand-name { font-family: "Anton", "Impact", sans-serif; fill: var(--white); letter-spacing: 1px; }
  .services { font-family: "Montserrat", sans-serif; font-weight: 700; fill: var(--white); letter-spacing: 1px; }
  .services .star { fill: var(--wrap-red); }
  .phone { font-family: "Montserrat", sans-serif; font-weight: 800; fill: var(--white); }
  .website { font-family: "Barlow Semi Condensed", sans-serif; font-weight: 700; fill: var(--wrap-black); }
  .feature { font-family: "Montserrat", sans-serif; font-weight: 700; fill: var(--white); font-size: 11px; }
  .chevron { fill: var(--wrap-red); }
  .offer-small { font-family: "Montserrat", sans-serif; font-weight: 600; fill: var(--white); }
  .offer-route { font-family: "Montserrat", sans-serif; font-weight: 800; fill: var(--white); }
  .offer-price { font-family: "Montserrat", sans-serif; font-weight: 700; fill: var(--white); }
  .map-placeholder { fill: var(--map-red); }
</style>
</head>
<body>
<div class="canvas">
  <svg class="van" viewBox="0 0 1200 688" xmlns="http://www.w3.org/2000/svg">
    <defs>
      <clipPath id="body-shape">
        <path d="M21 512 L26 380 Q32 342 61 328 L109 288 L246 158 Q290 116 335 108 L1087 100 Q1108 102 1116 123 L1158 320 L1162 512 L1030 512 A86 86 0 0 0 860 512 L345 512 A86 86 0 0 0 175 512 Z"/>
      </clipPath>
    </defs>

    <!-- Van body -->
    <g class="body" clip-path="url(#body-shape)">
      <rect x="0" y="80" width="1200" height="460" fill="var(--wrap-black)"/>
      <path class="red-band" fill="var(--wrap-red)"
            d="M104 361 L832 140 Q838 104 852 96 L1200 96 L1200 283 L1160 283 L453 454 Q414 468 410 500 L410 540 L104 540 Z"/>
      <path d="M165 198 L368 189 L350 283 L142 302 Z" fill="var(--glass)"/>
      <path d="M400 190 L400 520 M703 135 L705 520" stroke="var(--trim)" stroke-width="1" opacity="0.5" fill="none"/>
      <rect x="312" y="319" width="44" height="9" rx="4" fill="var(--wrap-black)"/>
      <rect x="427" y="312" width="11" height="32" rx="3" fill="var(--wrap-black)"/>
      <rect x="20" y="410" width="84" height="100" fill="var(--wrap-black)"/>
      <path d="M48 362 L102 362 L102 397 L46 397 Z" fill="#d8dde0"/>
      <rect x="1130" y="480" width="40" height="30" fill="var(--wrap-black)"/>

      <!-- New Zealand map area -->
      <rect class="map-placeholder" role="img" aria-label="Red map silhouette of New Zealand"
            x="1014" y="342" width="118" height="122" rx="14"/>
    </g>

    <!-- Mirror -->
    <path d="M140 258 Q150 252 158 256 L160 296 Q150 302 140 296 Z" fill="var(--wrap-black)"/>

    <!-- Wheels -->
    <g class="wheel">
      <circle cx="260" cy="517" r="72" fill="var(--tyre)"/>
      <circle cx="260" cy="517" r="46" fill="var(--hub)"/>
      <circle cx="260" cy="517" r="10" fill="#9aa0a5"/>
    </g>
    <g class="wheel">
      <circle cx="945" cy="517" r="72" fill="var(--tyre)"/>
      <circle cx="945" cy="517" r="46" fill="var(--hub)"/>
      <circle cx="945" cy="517" r="10" fill="#9aa0a5"/>
    </g>

    <!-- China map area -->
    <rect class="map-placeholder" role="img" aria-label="Red map silhouette of China"
          x="374" y="122" width="180" height="126" rx="16"/>

    <!-- Sea parcel offer -->
    <g class="offer">
      <text class="offer-small" x="452" y="188" font-size="10" text-anchor="middle">SEA PARCEL</text>
      <text class="offer-route" x="452" y="202" font-size="13" text-anchor="middle">CHINA <tspan font-weight="600">to</tspan> NZ</text>
      <text class="offer-price" x="405" y="231" font-size="29">$3<tspan font-size="14" dy="-12">.49</tspan><tspan font-size="13" font-weight="600">/kg</tspan></text>
      <rect x="448" y="227" width="50" height="2" fill="var(--white)"/>
    </g>

    <!-- Top features -->
    <g class="features-top">
      <path class="chevron" d="M571 145 L577 145 L583 155 L577 165 L571 165 L577 155 Z"/>
      <text class="feature" x="590" y="156">COMPETITIVE</text>
      <text class="feature" x="590" y="167">PRICING</text>
      <path class="chevron" d="M571 177 L577 177 L583 188 L577 199 L571 199 L577 188 Z"/>
      <text class="feature" x="590" y="187">INTERNATIONAL</text>
      <text class="feature" x="590" y="198">DELIVERY</text>
    </g>

    <!-- Contact -->
    <text class="phone" x="228" y="386" font-size="26" text-anchor="middle">09 4815396</text>
    <text class="website" x="228" y="404" font-size="15" text-anchor="middle">BOXWILLOW.CO.NZ</text>

    <!-- Brand name -->
    <text class="brand-name" x="0" y="0" font-size="150" textLength="600" lengthAdjust="spacingAndGlyphs"
          transform="translate(494 412) rotate(-13.4)">BOXWILLOW</text>

    <!-- Services -->
    <text class="services" x="0" y="0" font-size="25" textLength="590" lengthAdjust="spacingAndGlyphs"
          transform="translate(520 465) rotate(-13.4)"><tspan class="star">★</tspan> SEA PARCELS <tspan class="star">★</tspan> AIR PARCELS <tspan class="star">★</tspan> LOOSE CARGO</text>

    <!-- Bottom features -->
    <g class="features-bottom">
      <path class="chevron" d="M719 455 L725 455 L731 466 L725 477 L719 477 L725 466 Z"/>
      <text class="feature" x="738" y="464">SECURE PAYMENT</text>
      <text class="feature" x="738" y="475">METHODS</text>
      <path class="chevron" d="M719 485 L725 485 L731 496 L725 507 L719 507 L725 496 Z"/>
      <text class="feature" x="737" y="500">SHOP SAFELY</text>
    </g>
  </svg>
</div>
</body>
</html>
```